Banner to be used on our homepage as top filling

We want to show a good looking banner on the frontend of our website (its not live yet so we cant link to the website itself yet). I've added a screenshot impression of our website to give you an impression of our style.
The banner will be in the grey area of the "rw-concept.jpg" and will have a little bit of grey area left as a container around it.
Ofcourse underneath the banner we will add like a popular product selection and so on. But thats not important for this banner design.
The requirements of the banner is as followed:
- The banner should be in a 1280x720 dimension which should give plenty of space for visual elements in the banner
- The general color scheme of the banner needs to include our brand colors:
purple: '#92278F'
grey: '#6D6E71'
green complimentary: '#27912B'
- our logo icon needs to be in it (so just the circle with the RW triangle in it) incorporated in it, but not too obvious or as a distraction for what the banner is about. For example it could be semi transparent added to the background.
- We sell fighting equipment, so we need it to be appealing to our customer, but not be too aggresive. We focus on jiu jitsu and judo style martial arts, and do not reflect the aggression you see in boxing/kickboxing.
The banner will link to a category page where we sell GI (also called Kimonos) and for that reason it needs to have a call to action which makes the user click to see the collection of Gi we sell.
All 3 supplier brands need to be visible on the banner, as we do not want one of our suppliers to feel underrated.
If you choose to show real kimonos, please make sure all 3 brands are incorporated. Pictures can be found on our suppliers webpages. In this case also ensure it has both male and female on it. So that customers get a neutral perspective in the banner. (hey its almost 2023 right).
We also like vector created elements, so if you choose to go for a vector design elements instead of photo's, we will also not be disappointed. Aslong as it makes our homepage look good, we're open to everything.
The suppliers are:
https://brolvanworks.com/
https://peluskorastore.com/
https://venobra.com/
This banner will be permanent and not be seasonal, later on we will add a seasonal christmas banner and make this a slider, but for now, this is the "main" banner which customers see when they enter the website.

```html
<!DOCTYPE html>
<html lang="nl">
<head>
<meta charset="utf-8">
<title>RingWear – Gi collectie</title>
<link href="https://fonts.googleapis.com/css2?family=Arimo:wght@400;700&family=Poppins:wght@600;700&family=Roboto+Condensed:wght@400&family=Work+Sans:wght@500&display=swap" rel="stylesheet">
<style>
  :root {
    --purple: #92278F;
    --grey: #6D6E71;
    --green: #27912B;
    --header-bg: #000000;
    --hero-bg: #161616;
    --footer-bg: #000000;
    --link: #a9a9ad;
    --white: #ffffff;
    --subscribe: #c8420f;
  }
  * { box-sizing: border-box; margin: 0; padding: 0; }
  html, body { width: 1200px; height: 925px; overflow: hidden; background: var(--header-bg); }
  body { position: relative; font-family: "Arimo", Arial, sans-serif; color: var(--white); }

  .site-header { position: absolute; left: 0; top: 0; width: 1200px; height: 82px; background: var(--header-bg); }
  .brand { position: absolute; left: 82px; top: 22px; display: flex; align-items: center; gap: 10px; }
  .brand-mark { width: 38px; height: 38px; border-radius: 50%; background: var(--purple); }
  .brand-name { font-family: "Poppins", sans-serif; font-weight: 700; font-size: 26px; color: var(--purple); letter-spacing: .5px; }
  .menu-placeholder { position: absolute; left: 634px; top: 40px; transform: translate(-50%, -50%); font-weight: 700; font-size: 14px; }
  .header-icon { position: absolute; top: 30px; width: 20px; height: 20px; }
  .icon-search { left: 1037px; }
  .icon-cart { left: 1098px; }

  .hero { position: absolute; left: 0; top: 82px; width: 1200px; height: 607px; background: var(--hero-bg); overflow: hidden; }
  .hero-art { position: absolute; left: 0; top: 0; }
  .hero-title { position: absolute; left: 84px; top: 122px; width: 440px; font-family: "Roboto Condensed", sans-serif; font-weight: 400; font-size: 41px; line-height: 53px; }
  .cta { position: absolute; left: 82px; top: 313px; width: 278px; height: 46px; background: var(--green); border-radius: 3px; display: flex; align-items: center; justify-content: center; font-family: "Work Sans", sans-serif; font-weight: 500; font-size: 14.5px; color: var(--white); text-decoration: none; letter-spacing: .2px; }
  .suppliers-title { position: absolute; left: 84px; top: 417px; font-family: "Poppins", sans-serif; font-weight: 600; font-size: 23px; line-height: 30px; padding-bottom: 4px; border-bottom: 2px solid var(--purple); }
  .supplier-list { position: absolute; left: 82px; top: 470px; display: flex; gap: 26px; list-style: none; }
  .supplier { display: flex; align-items: center; gap: 7px; font-family: "Poppins", sans-serif; font-weight: 700; font-size: 21px; color: var(--white); }
  .supplier-dot { width: 30px; height: 30px; border-radius: 50%; background: var(--white); }

  .site-footer { position: absolute; left: 0; top: 689px; width: 1200px; height: 172px; background: var(--footer-bg); }
  .footer-col { position: absolute; top: 26px; }
  .footer-col h3 { font-size: 13.5px; font-weight: 700; letter-spacing: .6px; margin-bottom: 12px; }
  .footer-col ul { list-style: none; }
  .footer-col li { font-size: 13.5px; color: var(--link); line-height: 34px; }
  .col-service { left: 81px; } .col-company { left: 345px; } .col-brands { left: 609px; } .col-newsletter { left: 859px; }
  .newsletter-input { display: block; width: 246px; height: 35px; border: 1px solid #ccc; border-radius: 3px; padding: 0 10px; font-family: inherit; font-size: 13.5px; color: #666; background: var(--white); }
  .newsletter-button { position: absolute; left: 141px; top: 70px; width: 106px; height: 33px; border: 0; border-radius: 4px; background: var(--subscribe); color: var(--white); font-family: inherit; font-size: 13.5px; }

  .legal-bar { position: absolute; left: 0; top: 861px; width: 1200px; height: 64px; background: var(--purple); border-top: 1px solid var(--grey); display: flex; align-items: center; }
  .legal-name { position: absolute; left: 92px; font-size: 16px; color: #2a1a2a; }
  .legal-tagline { position: absolute; left: 258px; font-size: 13.5px; }
  .legal-handle { position: absolute; left: 717px; font-size: 13.5px; }
</style>
</head>
<body>
  <header class="site-header">
    <div class="brand"><span class="brand-mark"></span><span class="brand-name">RingWear</span></div>
    <nav class="menu-placeholder">Menu will be made here</nav>
    <svg class="header-icon icon-search" viewBox="0 0 20 20" fill="none" stroke="#fff" stroke-width="2"><circle cx="8" cy="8" r="6"/><line x1="12.5" y1="12.5" x2="18" y2="18"/></svg>
    <svg class="header-icon icon-cart" viewBox="0 0 20 20" fill="none" stroke="#fff" stroke-width="1.8"><path d="M1 2h3l2 10h10l2-7H5"/><circle cx="7.5" cy="16.5" r="1.5"/><circle cx="15" cy="16.5" r="1.5"/></svg>
  </header>

  <section class="hero">
    <svg class="hero-art" width="1200" height="607" viewBox="0 0 1200 607">
      <defs>
        <linearGradient id="photoTone" x1="0" y1="0" x2="1" y2="1">
          <stop offset="0" stop-color="#c9c9c9"/>
          <stop offset="0.45" stop-color="#8f96b8"/>
          <stop offset="0.75" stop-color="#3a4a9a"/>
          <stop offset="1" stop-color="#222"/>
        </linearGradient>
      </defs>
      <polygon points="566,0 1200,0 1200,607 678,607 514,94" fill="#d4d4d4"/>
      <g role="img" aria-label="Photo of a man in a blue gi and a woman in a black gi, both wearing black belts">
        <polygon points="608,0 1200,0 1200,607 690,607 580,380 564,94" fill="url(#photoTone)"/>
      </g>
      <polygon class="chevron" points="556,0 608,0 564,94 680,400 650,400 526,94" fill="var(--green)"/>
      <polygon class="chevron" points="580,383 622,383 690,607 676,607" fill="var(--green)"/>
    </svg>

    <h1 class="hero-title">We Sell Products For Jiu Jitsu And Judo Style Martial Arts</h1>
    <a class="cta" href="#gi-collectie">Click To See The Collection Of Gi</a>

    <h2 class="suppliers-title">OUR SUPPLIERS</h2>
    <ul class="supplier-list">
      <li class="supplier"><span class="supplier-dot"></span>VENOBRA</li>
      <li class="supplier"><span class="supplier-dot"></span>PELUSKORA</li>
      <li class="supplier">BROLVAN</li>
    </ul>
  </section>

  <footer class="site-footer">
    <div class="footer-col col-service"><h3>KLANTENSERVICE</h3><ul><li>Account</li><li>Mijn bestellingen</li></ul></div>
    <div class="footer-col col-company"><h3>RINGWEAR</h3><ul><li>About Us</li><li>Contact</li><li>Privacy Policy</li></ul></div>
    <div class="footer-col col-brands"><h3>OUR BRANDS</h3><ul><li>Brolvan Works</li><li>Venobra</li><li>Peluskora</li></ul></div>
    <div class="footer-col col-newsletter">
      <h3>NIEUWSBRIEF</h3>
      <input class="newsletter-input" type="email" placeholder="Voer uw e-mailadres in">
      <button class="newsletter-button" type="button">Inschrijven</button>
    </div>
  </footer>

  <div class="legal-bar">
    <span class="legal-name">RingWear V.O.F.</span>
    <span class="legal-tagline">Control, Balance, Fight! - Top kwaliteit vechtsport artikelen - Nederland</span>
    <span class="legal-handle">@RingWear</span>
  </div>
</body>
</html>
```